Jewelers Website

This is for the DESIGN ONLY.
I am a software programmer and will be doing the development.
New website design for
www.lumaoakstones.com.au
Need a fresh new look for an online only jewellery business who produce their jewellery by hand. I would like it designed in a parallax style. Feel free to recommend fonts to use for the site. This is an Australian based company located in NSW so shots of sites in NSW might make nice background images.
http://brixolatemplates.net/demo/#theme=parallax
To contain the below sections
About Us
Contact Us
Gallery
Testimonials
Diamond Types
The colour scheme is to be Black / White and Silver.
With the Parallax style there will be moving sections and images for added impact.
Target Market(s)
Young Adults mainly engagement jewellery
Industry/Entity Type
Software
Look and feel

```html
<!DOCTYPE html>
<html lang="en">
<head>
<meta charset="utf-8">
<title>Luma Oak Stones – Team, Testimonial and Contact</title>
<link rel="stylesheet" href="https://fonts.googleapis.com/css2?family=Lato:ital,wght@0,300;0,400;0,700;0,900;1,700&display=swap">
<style>
  :root {
    --ink: #000;
    --white: #fff;
    --team-dark: #0d0d0d;
    --team-mid: #2a2a2a;
    --subtitle: #b9b9b9;
    --button-text: #7a7a7a;
    --quote-light: #f7f7f8;
    --quote-mid: #e4e5e7;
    --footer-bg: #1c1c1c;
    --footer-text: #e6e6e6;
    --footer-rule: #444;
    --submit-bg: #c9c9c9;
    --portrait-light: #cfcfcf;
    --portrait-dark: #6f6a66;
  }
  * { margin: 0; padding: 0; box-sizing: border-box; }
  html, body { width: 1200px; height: 1197px; overflow: hidden; }
  body { position: relative; font-family: "Lato", sans-serif; background: var(--footer-bg); }
  .abs { position: absolute; }

  /* Team */
  .team {
    position: absolute; left: 0; top: 0; width: 1200px; height: 572px;
    background: radial-gradient(ellipse at 50% 40%, var(--team-mid), var(--team-dark) 75%);
  }
  .team-rule { position: absolute; top: 61px; left: 292px; width: 629px; height: 1px; background: var(--white); }
  .team-title {
    position: absolute; top: 42px; left: 0; width: 1200px; text-align: center;
    color: var(--white); font-weight: 700; font-size: 31px; line-height: 38px;
  }
  .team-subtitle {
    position: absolute; top: 79px; left: 0; width: 1200px; text-align: center;
    color: var(--subtitle); font-weight: 300; font-size: 15px;
  }
  .member { position: absolute; top: 170px; width: 220px; margin-left: -110px; text-align: center; }
  .portrait {
    width: 166px; height: 166px; border-radius: 50%; margin: 0 auto;
    background: radial-gradient(circle at 50% 45%, var(--portrait-light), var(--portrait-dark));
  }
  .member-name { margin-top: 28px; color: var(--white); font-weight: 700; font-size: 26px; }
  .view-all {
    position: absolute; left: 551px; top: 444px; width: 102px; height: 36px;
    background: var(--white); color: var(--button-text); font-size: 14px; font-weight: 700;
    line-height: 36px; text-align: center;
  }

  /* Testimonial */
  .testimonial {
    position: absolute; left: 0; top: 572px; width: 1200px; height: 240px;
    background: linear-gradient(160deg, var(--quote-light), var(--quote-mid) 55%, var(--quote-light));
  }
  .quote-mark { position: absolute; left: 220px; top: 592px; }
  .quote-text {
    position: absolute; left: 300px; top: 595px; width: 600px; text-align: center;
    font-weight: 700; font-size: 17px; line-height: 42px; color: var(--ink);
  }
  .quote-author {
    position: absolute; left: 0; top: 738px; width: 1200px; text-align: center;
    font-weight: 700; font-style: italic; font-size: 36px; color: var(--ink);
  }

  /* Footer */
  .footer-heading { position: absolute; top: 848px; font-weight: 300; font-size: 26px; color: var(--footer-text); }
  .nav-list { position: absolute; left: 88px; top: 902px; list-style: none; }
  .nav-list li { font-weight: 300; font-size: 17px; color: var(--footer-text); height: 37.5px; }
  .legal-small { position: absolute; left: 120px; top: 1082px; font-family: Arial, sans-serif; font-size: 11px; color: var(--footer-text); }
  .address-block { position: absolute; left: 336px; font-weight: 300; font-size: 16px; line-height: 20px; color: var(--footer-text); }
  .social-dot { position: absolute; top: 1071px; width: 21px; height: 21px; border-radius: 50%; background: var(--white); }
  .field {
    position: absolute; border: 2px solid var(--white); border-radius: 8px;
    color: var(--footer-text); font-size: 16px; padding: 9px 12px;
  }
  .submit {
    position: absolute; left: 985px; top: 1061px; width: 125px; height: 34px; border-radius: 5px;
    background: var(--submit-bg); color: var(--white); font-size: 15px; text-align: center; line-height: 34px;
  }
  .footer-rule { position: absolute; left: 0; top: 1129px; width: 1200px; height: 1px; background: var(--footer-rule); }
  .copyright { position: absolute; left: 88px; top: 1155px; font-family: Arial, sans-serif; font-size: 12px; color: var(--footer-text); }
</style>
</head>
<body>

<section class="team" role="img" aria-label="Dark woven carbon fibre texture background"></section>
<div class="team-rule"></div>
<h2 class="team-title">MEET OUR TEAM</h2>
<p class="team-subtitle">Lorem ipsum dolor sit amet, consectetur adipisicing</p>

<div class="member" style="left:270px"><div class="portrait" role="img" aria-label="Portrait photo of Jhony Den"></div><p class="member-name">Jhony Den</p></div>
<div class="member" style="left:490px"><div class="portrait" role="img" aria-label="Portrait photo of Elisa Deny"></div><p class="member-name">Elisa Deny</p></div>
<div class="member" style="left:712px"><div class="portrait" role="img" aria-label="Portrait photo of Randy Bear"></div><p class="member-name">Randy Bear</p></div>
<div class="member" style="left:933px"><div class="portrait" role="img" aria-label="Portrait photo of Anna Hart"></div><p class="member-name">Anna Hart</p></div>

<div class="view-all">View All</div>

<section class="testimonial" role="img" aria-label="Soft silver abstract wave background"></section>
<svg class="quote-mark" width="66" height="48" viewBox="0 0 66 48" aria-hidden="true">
  <g fill="#000">
    <circle cx="14" cy="32" r="11"/><path d="M3 32 C3 18 10 8 22 5 L23 9 C14 12 10 19 10 27 Z"/>
    <circle cx="50" cy="32" r="11"/><path d="M39 32 C39 18 46 8 58 5 L59 9 C50 12 46 19 46 27 Z"/>
  </g>
</svg>
<p class="quote-text">Anytime I had a question, I just gave support a call and&nbsp; they picked up right away. I just can't say enough about how great those guys are.</p>
<p class="quote-author">John Doe</p>

<!-- Footer -->
<h3 class="footer-heading" style="left:86px">Navigation</h3>
<h3 class="footer-heading" style="left:312px">Address</h3>
<h3 class="footer-heading" style="left:677px">Contact Us</h3>

<ul class="nav-list">
  <li>Home</li><li>About Us</li><li>Properties</li><li>Contact Us</li>
</ul>
<p class="legal-small">Copyright@2014 PRIVACY POLICY</p>

<svg class="abs" style="left:308px;top:906px" width="14" height="14" viewBox="0 0 14 14" aria-hidden="true"><path d="M13 1 L1 6 L6 8 L8 13 Z" fill="#fff"/></svg>
<div class="address-block" style="top:903px">Sydney<br>Marrowvale NSW 2291, Australia<br>Germany<br>52817 Lindenfeld, Germany</div>

<svg class="abs" style="left:307px;top:1001px" width="16" height="16" viewBox="0 0 16 16" aria-hidden="true"><path d="M3 1 L6 1 L7 5 L5 6.5 C6 9 7.5 10.5 10 11.5 L11.5 9.5 L15 10.5 L15 13.5 C15 14.5 14 15 13 15 C6 14 2 10 1 3 C1 2 2 1 3 1 Z" fill="#fff"/></svg>
<div class="address-block" style="top:998px;font-size:17px;line-height:25px">+61 (0)2 9483 2710<br>+49 (0)2168 5270413</div>

<div class="social-dot" style="left:337px"></div>
<div class="social-dot" style="left:371px"></div>
<div class="social-dot" style="left:406px"></div>
<div class="social-dot" style="left:440px"></div>

<div class="field" style="left:679px;top:897px;width:170px;height:45px">Name</div>
<div class="field" style="left:869px;top:897px;width:242px;height:45px">Email</div>
<div class="field" style="left:679px;top:959px;width:432px;height:86px">Message</div>
<div class="submit">Submit</div>

<div class="footer-rule"></div>
<p class="copyright">© Copyright 2002-2012 Luma Oak Stones Pty Ltd(ABN 47 208 615 902)</p>

</body>
</html>
```